Vel-Trax.ch is looking for business card letterhead and envelope C5 with WOW effect

We need a strong business card for our company Vel-Trax.ch, logo is available. You want a black or dark background on which the logo Stark r% 26 # 252; appears. Letterhead and envelope in C5 format should be in a similar design, but does not have to be We need a strong business card for our company Vel-Trax.ch, logo is available. A black or dark background is desired, on which the logo Stark comes across. The letterhead and the envelope in C5 format should have a similar design.

Target Market(s)

Private customers as well as entrepreneurs

Contact Information for Business Card

E-mail: info@vel-trax.ch
Web.www.Vel-Trax.ch
Tel: +41 ( 0 ) 79 684 3027
Adresse:
Lindenhaldeweg 14
9403 Brenzikon

Hier kann man Icons verwenden für Email,Tel und Adressse

Font styles to use
Other font styles liked:
• Dubai,bold

Colors

Designer to choose colors to be used in the design.

Requirements
Must have
• WOW effect
Nice to have
• R% 26 # 252; back business card with our service listings. - VEHICLE LABELING - SHOP WINDOW LABELING - STICKERS AND MUCH MORE ... in red color

```html
<!DOCTYPE html>
<html lang="en">
<head>
<meta charset="utf-8">
<title>Vel-Trax.ch business card</title>
<link rel="stylesheet" href="https://fonts.googleapis.com/css2?family=Ubuntu:wght@400;500;700&display=swap">
<style>
  :root {
    --bg: #8d949a;
    --card: #222222;
    --card-edge: #1a1a1a;
    --yellow: #fdc516;
    --grey: #b9b9b9;
  }
  * { margin: 0; padding: 0; box-sizing: border-box; }
  html, body { width: 1200px; height: 913px; overflow: hidden; }
  body {
    background: var(--bg);
    font-family: "Ubuntu", Arial, sans-serif;
    position: relative;
  }
  .card {
    position: absolute;
    width: 640px;
    height: 370px;
    background: var(--card);
    border-radius: 4px;
    box-shadow: 0 3px 0 var(--card-edge), 0 6px 0 #2c2c2c, 0 14px 28px rgba(0,0,0,.35);
    overflow: hidden;
  }
  .card--front { left: 60px; top: 70px; }
  .card--back { left: 500px; top: 470px; }

  .pattern-area {
    position: absolute;
    border-radius: 6px;
    background: linear-gradient(135deg, rgba(253,197,22,.85) 0%, rgba(253,197,22,.55) 55%, rgba(253,197,22,.25) 100%);
  }
  .card--front .pattern-area { left: 40px; top: 140px; width: 240px; height: 190px; }
  .card--back .pattern-area { left: 40px; top: 110px; width: 300px; height: 220px; }

  .wordmark {
    position: absolute;
    right: 40px;
    top: 52px;
    color: var(--yellow);
    font-weight: 700;
    font-size: 50px;
    letter-spacing: 1px;
    line-height: 1;
    white-space: nowrap;
  }
  .services {
    position: absolute;
    right: 40px;
    top: 140px;
    list-style: none;
    text-align: right;
  }
  .services li {
    color: var(--yellow);
    font-weight: 700;
    font-size: 15px;
    line-height: 24px;
    display: flex;
    align-items: center;
    justify-content: flex-end;
    gap: 10px;
    white-space: nowrap;
  }
  .services li::after {
    content: "";
    width: 10px;
    height: 10px;
    border-radius: 50%;
    background: var(--yellow);
  }

  .person {
    position: absolute;
    right: 40px;
    top: 38px;
    text-align: right;
  }
  .person__name {
    color: var(--yellow);
    font-weight: 700;
    font-size: 26px;
    letter-spacing: .5px;
  }
  .person__role {
    color: var(--grey);
    font-size: 15px;
    letter-spacing: 1px;
    margin-top: 2px;
  }
  .address {
    position: absolute;
    right: 40px;
    top: 140px;
    text-align: right;
    color: var(--grey);
    font-size: 15px;
    line-height: 22px;
    font-style: normal;
  }
  .divider {
    position: absolute;
    right: 40px;
    top: 195px;
    width: 70px;
    height: 2px;
    background: var(--yellow);
  }
  .contact {
    position: absolute;
    right: 40px;
    top: 212px;
    list-style: none;
  }
  .contact li {
    color: var(--grey);
    font-size: 15px;
    line-height: 26px;
    display: flex;
    align-items: center;
    justify-content: flex-end;
    gap: 10px;
  }
  .contact svg { width: 16px; height: 16px; fill: var(--yellow); flex: none; }
</style>
</head>
<body>
  <section class="card card--front" aria-label="Business card front">
    <div class="pattern-area" role="img" aria-label="Honeycomb pattern of yellow filled and outlined hexagons"></div>
    <div class="wordmark">VEL-TRAX.CH</div>
    <ul class="services">
      <li>VEHICLE LABELING</li>
      <li>SHOP WINDOW LABELING</li>
      <li>STICKERS AND MUCH MORE</li>
    </ul>
  </section>

  <section class="card card--back" aria-label="Business card back">
    <div class="pattern-area" role="img" aria-label="Honeycomb pattern of yellow filled and outlined hexagons"></div>
    <div class="person">
      <div class="person__name">ADRIAN KELLER</div>
      <div class="person__role">DIRECTOR</div>
    </div>
    <address class="address">Lindenhaldeweg 14<br>9403 Brenzikon</address>
    <div class="divider"></div>
    <ul class="contact">
      <li>+41 ( 0 ) 79 684 3027
        <svg viewBox="0 0 16 16" aria-hidden="true"><path d="M3.5 1.5l2.5 0 1 3.5-1.8 1.2a8 8 0 0 0 4.6 4.6L11 9l3.5 1v2.5c0 1-1 2-2 2C6.5 14.5 1.5 9.5 1.5 3.5c0-1 1-2 2-2z"/></svg>
      </li>
      <li>info@vel-trax.ch
        <svg viewBox="0 0 16 16" aria-hidden="true"><path d="M1 3.5h14v9H1z M1.5 4l6.5 5 6.5-5" fill="none" stroke="#fdc516" stroke-width="1.6"/></svg>
      </li>
      <li>www.Vel-Trax.ch
        <svg viewBox="0 0 16 16" aria-hidden="true"><circle cx="8" cy="8" r="6.5" fill="none" stroke="#fdc516" stroke-width="1.5"/><path d="M1.5 8h13M8 1.5c-3 3.5-3 9.5 0 13M8 1.5c3 3.5 3 9.5 0 13" fill="none" stroke="#fdc516" stroke-width="1.2"/></svg>
      </li>
    </ul>
  </section>
</body>
</html>
```